Online Dating Website called WinkAtWheel.net

PLEASE CAN ALL PARTICIPATING DESIGNERS PLEASE SUBMIT ALL PAGES AS DETAILED IN THE ORIGINAL BRIEF BELOW WITHIN 48 HOURS TO AVOID WINKATWHEEL EXTENDING THE CONTEST FURTHER.

We have an online dating website that is 95% fully functional and now require an exciting and creative designer to help us create the best dating experience. We are looking for your ideas on a couple of our key pages. These are our landing, profile and search page. We already have a homepage that we are happy with and winning designers will look to build upon the foundations of the homepage and extend them through their designs.

The premise of the site is the idea that if you've ever seen someone out driving and wished you could communicate because you found them attractive, how would you? Well with WinkAtWheel.net you can. Just enter their vehicle registration number (license plate) in to the website in order to get in touch, flirt and develop a relationship. It also allows users to find each other based on other criteria. It acts as both a specialist service and a normal dating website.

The pages that require developing are 1) our landing page, this is the page users see when they first login to the site, it comprises various pieces of information but it's primary function is a live feed of events generated based on the users favourited profiles and interactions with the user. 2) The profile page is the page where users can edit their own information, given the nature of this page we are looking for a creative design that gives this page some flair. 3) Finally we are looking for ideas for our search page, this page needs to provide a list of users who meet the user's search requirements and display the profile of a selected user.
Updates

Project Deadline Extended
Reason: We've asked for certain pages in our brief to be designed and this still hasn't been done. We've contacted the designers that have currently submitted designs and requested this several times. We still await for this to happen.

Target Market(s)

Male or Female age 18+

Industry/Entity Type

Dating

Requirements
Must have
• Our must have feature is a designer with an open mind. The functionality of the site must be present, all we ask is for you to be creative with the layout. Think out side of the box, change the colours, the layout, and the background as you feel. Make it look current and appealing to the user.
Nice to have
• Theme's carried through from the home page
Should not have
• Do not include Comic Sans or Times New Roman font in your designs.

```html
<!DOCTYPE html>
<html lang="en">
<head>
<meta charset="utf-8">
<title>WinkAtWheel.net – Dashboard</title>
<link href="https://fonts.googleapis.com/css2?family=Play:wght@400;700&family=Arimo:wght@400&display=swap" rel="stylesheet">
<style>
:root{
  --header-top:#1c1c1c;
  --header-mid:#3a3a3a;
  --green:#82ac48;
  --blue:#2b7fd4;
  --blue-dark:#1f6bbd;
  --panel:#d9d9d9;
  --panel-dark:#b3b3b3;
  --card-head:#333333;
  --ink:#222222;
  --muted:#666666;
  --white:#ffffff;
  --pink:#e0197d;
  --tick:#7aa43a;
  --photo:#c8c8c8;
}
*{box-sizing:border-box;margin:0;padding:0}
html,body{width:1153px;height:1200px;overflow:hidden;background:var(--white)}
body{position:relative;font-family:"Arimo",Arial,sans-serif;color:var(--ink)}
.display{font-family:"Play",sans-serif}
.abs{position:absolute}

/* header */
.site-header{left:0;top:0;width:1153px;height:80px;background:linear-gradient(var(--header-top),var(--header-mid) 55%,var(--header-top))}
.brand{left:138px;top:16px;display:flex;align-items:center;gap:10px;font-family:"Play",sans-serif;font-size:30px;color:var(--white)}
.brand-dot{width:22px;height:22px;border-radius:50%;background:var(--blue)}
.main-nav{top:28px;font-family:"Play",sans-serif;font-weight:700;font-size:15px;color:var(--white)}
.account-menu{left:893px;top:22px;width:99px;height:73px;font-family:"Play",sans-serif;font-weight:700;color:var(--white)}
.account-tab{position:absolute;left:0;top:0;width:99px;height:30px;background:var(--blue);border-radius:4px 4px 0 0;padding:8px 0 0 13px;font-size:14px}
.account-drop{position:absolute;left:-17px;top:29px;width:116px;height:44px;background:var(--blue);padding:4px 0 0 9px;font-size:13px;line-height:18px}

/* quick search */
.quick-search{left:137px;top:100px;width:858px;height:56px;background:var(--green)}
.quick-search .label{position:absolute;left:13px;top:16px;font-family:"Play",sans-serif;font-weight:700;font-size:19px;color:var(--white)}
.field{position:absolute;top:12px;height:31px;background:var(--white);border:1px solid #cfcfcf;font-size:13px;color:#666;padding:8px 0 0 9px}
.field svg{position:absolute;right:10px;top:12px}
.btn-dark{background:linear-gradient(#3c3c3c,#050505);color:var(--white);border-radius:4px;font-family:"Play",sans-serif;font-weight:700;text-align:center}
.quick-search .btn-dark{position:absolute;left:713px;top:13px;width:124px;height:32px;font-size:17px;line-height:32px}

/* welcome panel */
.welcome{left:137px;top:156px;width:858px;height:235px;background:var(--panel)}
.welcome h1{position:absolute;left:14px;top:11px;font-family:"Play",sans-serif;font-weight:700;font-size:23px;color:var(--ink)}
.avatar{background:var(--white);padding:12px}
.avatar .photo{width:100%;height:100%;background:linear-gradient(var(--photo),#bdbdbd)}
.welcome .avatar{position:absolute;left:15px;top:56px;width:120px;height:120px}
.member-name{position:absolute;left:150px;top:56px;font-family:"Play",sans-serif;font-weight:700;font-size:22px}
.member-meta{position:absolute;left:150px;top:85px;font-family:"Play",sans-serif;font-weight:700;font-size:14px;color:#777}
.status-input{position:absolute;left:148px;top:111px;width:125px;height:25px;background:var(--white);border:1px solid #bbb;font-size:12px;color:#555;padding:5px 0 0 8px}
.welcome .btn-dark{position:absolute;left:279px;top:110px;width:71px;height:25px;font-size:14px;line-height:25px}
.btn-blue{position:absolute;top:145px;height:28px;background:linear-gradient(#3a92e6,var(--blue-dark));border-radius:5px;color:var(--white);font-family:"Play",sans-serif;font-weight:700;font-size:14px;text-align:center;line-height:28px}

.status-box{position:absolute;left:369px;top:56px;width:476px;height:165px;background:var(--panel-dark);border-radius:6px;overflow:hidden}
.status-box .tab{height:27px;background:var(--white);border-radius:6px 6px 0 0;padding:2px 0 0 14px;font-family:"Play",sans-serif;font-weight:700;font-size:18px}
.stat-col{position:absolute;top:36px;width:139px}
.stat-col h3{font-family:"Play",sans-serif;font-weight:700;font-size:15px;text-align:center;padding-bottom:4px;border-bottom:1px solid #7a7a7a}
.stat-col ul{list-style:none;margin-top:10px;font-size:12.5px;line-height:19px}
.stat-col li span{display:inline-block;width:97px}

/* sidebar */
.side-panel{left:138px;width:254px;background:var(--panel)}
.side-panel .head{height:35px;background:var(--green);color:var(--white);font-family:"Play",sans-serif;font-weight:700;font-size:18px;padding:7px 0 0 11px}
.match-list{list-style:none;margin:8px 0 0 11px;font-size:11.5px;line-height:20.6px}
.match-list li{display:flex;align-items:center;gap:7px}
.thumbs{display:grid;grid-template-columns:repeat(3,73px);gap:7px;margin:15px 0 0 11px}
.thumb{height:73px;background:#555;padding:4px}
.thumb div{width:100%;height:100%;background:radial-gradient(circle at 50% 55%,#d8cfc4,#8a7a6a 55%,#2a2622)}
.filter h4{font-family:"Play",sans-serif;font-weight:700;font-size:15px;margin:12px 0 0 11px}
.filter ul{list-style:none;margin:2px 0 0 12px;width:223px;font-size:12.6px;line-height:21px;color:#333}
.filter li{display:flex;justify-content:space-between;align-items:center}

/* feed */
.feed-card{left:412px;width:584px;height:180px;background:var(--panel)}
.feed-card .head{height:34px;background:var(--card-head);color:var(--white);font-family:"Play",sans-serif;font-weight:700;font-size:18px;padding:5px 0 0 11px}
.feed-card .avatar{position:absolute;left:11px;top:47px;width:120px;height:120px}
.feed-card p{position:absolute;left:144px;top:47px;width:430px;font-size:12.6px;line-height:16.2px;color:#333}
</style>
</head>
<body>

<header class="site-header abs">
  <div class="brand abs"><span>winkatwheel</span><span class="brand-dot"></span></div>
  <nav>
    <span class="main-nav abs" style="left:419px">Home</span>
    <span class="main-nav abs" style="left:483px">Profile</span>
    <span class="main-nav abs" style="left:556px">Messages</span>
    <span class="main-nav abs" style="left:659px">Matches</span>
    <span class="main-nav abs" style="left:744px">Search</span>
    <span class="main-nav abs" style="left:820px">Support</span>
  </nav>
  <div class="account-menu abs">
    <div class="account-tab">My Account</div>
    <div class="account-drop">Logout<br>&nbsp;Profile</div>
  </div>
</header>

<section class="quick-search abs">
  <span class="label">Seen Someone?</span>
  <div class="field" style="left:171px;width:163px">Search</div>
  <div class="field" style="left:346px;width:163px">Make
    <svg width="18" height="9" viewBox="0 0 18 9"><path d="M0 0H18L9 9Z" fill="#888"/></svg></div>
  <div class="field" style="left:520px;width:163px">Colour
    <svg width="18" height="9" viewBox="0 0 18 9"><path d="M0 0H18L9 9Z" fill="#888"/></svg></div>
  <div class="btn-dark">Search</div>
</section>

<section class="welcome abs">
  <h1>Welcome our site is currently free during beta testing.</h1>
  <div class="avatar"><div class="photo" role="img" aria-label="Member profile photo placeholder"></div></div>
  <div class="member-name">Lee</div>
  <div class="member-meta">24 years old- larkford</div>
  <div class="status-input">How are you?</div>
  <div class="btn-dark">Update</div>
  <div class="btn-blue" style="left:148px;width:86px">Profile</div>
  <div class="btn-blue" style="left:244px;width:86px">Upload</div>

  <div class="status-box">
    <div class="tab">your status</div>
    <div class="stat-col" style="left:9px">
      <h3>likes 124</h3>
      <ul><li><span>Lorem Ipsum</span>20</li><li><span>Lorem Ipsum</span>20</li><li><span>Lorem Ipsum</span>20</li><li><span>Lorem Ipsum</span>20</li></ul>
    </div>
    <div class="stat-col" style="left:166px">
      <h3>Messages 171</h3>
      <ul><li><span>Lorem Ipsum</span>20</li><li><span>Lorem Ipsum</span>20</li><li><span>Lorem Ipsum</span>20</li><li><span>Lorem Ipsum</span>20</li></ul>
    </div>
    <div class="stat-col" style="left:324px">
      <h3>Favourites 20</h3>
      <ul><li><span>Lorem Ipsum</span>20</li><li><span>Lorem Ipsum</span>20</li><li><span>Lorem Ipsum</span>20</li><li><span>Lorem Ipsum</span>20</li></ul>
    </div>
  </div>
</section>

<aside class="side-panel abs" style="top:410px;height:335px">
  <div class="head">Your Matches</div>
  <ul class="match-list">
    <li><svg width="11" height="9" viewBox="0 0 11 9"><rect y="2" width="11" height="7" rx="1" fill="var(--pink)"/><rect x="3" width="5" height="3" fill="var(--pink)"/><circle cx="5.5" cy="5.5" r="2" fill="#fff"/></svg>Lorem Ipsum is simply dummy text</li>
    <li><svg width="11" height="9" viewBox="0 0 11 9"><rect y="2" width="11" height="7" rx="1" fill="var(--pink)"/><rect x="3" width="5" height="3" fill="var(--pink)"/><circle cx="5.5" cy="5.5" r="2" fill="#fff"/></svg>Lorem Ipsum is simply dummy text</li>
    <li><svg width="11" height="9" viewBox="0 0 11 9"><rect y="2" width="11" height="7" rx="1" fill="var(--pink)"/><rect x="3" width="5" height="3" fill="var(--pink)"/><circle cx="5.5" cy="5.5" r="2" fill="#fff"/></svg>Lorem Ipsum is simply dummy text</li>
    <li><svg width="11" height="9" viewBox="0 0 11 9"><rect y="2" width="11" height="7" rx="1" fill="var(--pink)"/><rect x="3" width="5" height="3" fill="var(--pink)"/><circle cx="5.5" cy="5.5" r="2" fill="#fff"/></svg>Lorem Ipsum is simply dummy text</li>
    <li><svg width="11" height="9" viewBox="0 0 11 9"><rect y="2" width="11" height="7" rx="1" fill="var(--pink)"/><rect x="3" width="5" height="3" fill="var(--pink)"/><circle cx="5.5" cy="5.5" r="2" fill="#fff"/></svg>Lorem Ipsum is simply dummy text</li>
    <li><svg width="11" height="9" viewBox="0 0 11 9"><rect y="2" width="11" height="7" rx="1" fill="var(--pink)"/><rect x="3" width="5" height="3" fill="var(--pink)"/><circle cx="5.5" cy="5.5" r="2" fill="#fff"/></svg>Lorem Ipsum is simply dummy text</li>
  </ul>
  <div class="thumbs">
    <div class="thumb"><div role="img" aria-label="Match photo"></div></div>
    <div class="thumb"><div role="img" aria-label="Match photo"></div></div>
    <div class="thumb"><div role="img" aria-label="Match photo"></div></div>
    <div class="thumb"><div role="img" aria-label="Match photo"></div></div>
    <div class="thumb"><div role="img" aria-label="Match photo"></div></div>
    <div class="thumb"><div role="img" aria-label="Match photo"></div></div>
  </div>
</aside>

<aside class="side-panel filter abs" style="top:771px;height:335px">
  <div class="head">Feed Filter</div>
  <h4>Status Updates</h4>
  <ul>
    <li>Lorem Ipsum is simply dummy text<svg width="20" height="16" viewBox="0 0 20 16"><path d="M1 9l6 6L19 2" fill="none" stroke="var(--tick)" stroke-width="4"/></svg></li>
    <li>Lorem Ipsum is simply dummy text<svg width="20" height="16" viewBox="0 0 20 16"><path d="M1 9l6 6L19 2" fill="none" stroke="var(--tick)" stroke-width="4"/></svg></li>
    <li>Lorem Ipsum is simply dummy text<span></span></li>
    <li>Lorem Ipsum is simply dummy text<svg width="20" height="16" viewBox="0 0 20 16"><path d="M1 9l6 6L19 2" fill="none" stroke="var(--tick)" stroke-width="4"/></svg></li>
    <li>Lorem Ipsum is simply dummy text<svg width="20" height="16" viewBox="0 0 20 16"><path d="M1 9l6 6L19 2" fill="none" stroke="var(--tick)" stroke-width="4"/></svg></li>
  </ul>
  <h4>Images Upload</h4>
  <ul>
    <li>Lorem Ipsum is simply dummy text<svg width="20" height="16" viewBox="0 0 20 16"><path d="M1 9l6 6L19 2" fill="none" stroke="var(--tick)" stroke-width="4"/></svg></li>
    <li>Lorem Ipsum is simply dummy text<svg width="20" height="16" viewBox="0 0 20 16"><path d="M1 9l6 6L19 2" fill="none" stroke="var(--tick)" stroke-width="4"/></svg></li>
    <li>Lorem Ipsum is simply dummy text<span></span></li>
    <li>Lorem Ipsum is simply dummy text<svg width="20" height="16" viewBox="0 0 20 16"><path d="M1 9l6 6L19 2" fill="none" stroke="var(--tick)" stroke-width="4"/></svg></li>
    <li>Lorem Ipsum is simply dummy text<svg width="20" height="16" viewBox="0 0 20 16"><path d="M1 9l6 6L19 2" fill="none" stroke="var(--tick)" stroke-width="4"/></svg></li>
  </ul>
</aside>

<article class="feed-card abs" style="top:410px">
  <div class="head">Lady changed her status</div>
  <div class="avatar"><div class="photo" role="img" aria-label="Member profile photo placeholder"></div></div>
  <p>Lorem Ipsum is simply dummy text of the printing and typesetting industry. Lorem Ipsum has been the industry's standard dummy text ever since the 1500s, when an unknown printer took a galley of type and scrambled it to make a type specimen book. It has survived not only five centuries, but also the leap into electronic typesetting, remaining essentially unchanged. It was popularised in the 1960s with the release of Letraset sheets containing</p>
</article>
<article class="feed-card abs" style="top:606px">
  <div class="head">Lady changed her status</div>
  <div class="avatar"><div class="photo" role="img" aria-label="Member profile photo placeholder"></div></div>
  <p>Lorem Ipsum is simply dummy text of the printing and typesetting industry. Lorem Ipsum has been the industry's standard dummy text ever since the 1500s, when an unknown printer took a galley of type and scrambled it to make a type specimen book. It has survived not only five centuries, but also the leap into electronic typesetting, remaining essentially unchanged. It was popularised in the 1960s with the release of Letraset sheets containing</p>
</article>
<article class="feed-card abs" style="top:800px">
  <div class="head">Lady changed her status</div>
  <div class="avatar"><div class="photo" role="img" aria-label="Member profile photo placeholder"></div></div>
  <p>Lorem Ipsum is simply dummy text of the printing and typesetting industry. Lorem Ipsum has been the industry's standard dummy text ever since the 1500s, when an unknown printer took a galley of type and scrambled it to make a type specimen book. It has survived not only five centuries, but also the leap into electronic typesetting, remaining essentially unchanged. It was popularised in the 1960s with the release of Letraset sheets containing</p>
</article>
<article class="feed-card abs" style="top:995px">
  <div class="head">Lady changed her status</div>
  <div class="avatar"><div class="photo" role="img" aria-label="Member profile photo placeholder"></div></div>
  <p>Lorem Ipsum is simply dummy text of the printing and typesetting industry. Lorem Ipsum has been the industry's standard dummy text ever since the 1500s, when an unknown printer took a galley of type and scrambled it to make a type specimen book. It has survived not only five centuries, but also the leap into electronic typesetting, remaining essentially unchanged. It was popularised in the 1960s with the release of Letraset sheets containing</p>
</article>

</body>
</html>
```